Business Card Design

Just looking for a good designs that looks good with our company logo. I'd like it to be simple and to the point. Just including contact information, our logo, and my name somewhere on the card so future clients know who they're contacting, and a couple services offered. The two images I attached are pictures of our logo. I don't care which color they they are, I just attached both images to give a reference of logo colors depending on the color of the card.
Names: Calvin Prewitt
Phone: 555-247-9061
Email: tidyturfcrew@mailvista.net
Services offered:
Mowing
Fertilization
Aeration
Bed & tree maintenance
and more.
Industry/Entity Type
Business
Contact Information for Business Card
Names: Calvin Prewitt
Phone: 555-247-9061
Look and feel

```html
<!DOCTYPE html>
<html lang="en">
<head>
<meta charset="utf-8">
<title>Tidy Turf Crew – Business Card</title>
<link href="https://fonts.googleapis.com/css2?family=Questrial&display=swap" rel="stylesheet">
<style>
  :root {
    --paper: #ffffff;
    --ink: #111111;
    --navy: #1c2a48;
    --red: #ee1c25;
    --red-soft: #f26a70;
    --grey-soft: #e4e4e4;
  }
  html, body {
    margin: 0;
    padding: 0;
    overflow: hidden;
    background: var(--paper);
  }
  .card {
    position: relative;
    width: 702px;
    height: 1200px;
    background: var(--paper);
    overflow: hidden;
    font-family: "Questrial", sans-serif;
    color: var(--ink);
  }
  .brand {
    position: absolute;
    top: 200px;
    left: 0;
    width: 702px;
    display: flex;
    align-items: center;
    justify-content: center;
    gap: 22px;
  }
  .brand-dot {
    width: 44px;
    height: 44px;
    border-radius: 50%;
    background: var(--red);
    flex: none;
  }
  .brand-name {
    font-size: 60px;
    letter-spacing: 2px;
    color: var(--navy);
    text-transform: uppercase;
    white-space: nowrap;
  }
  .contact {
    position: absolute;
    top: 484px;
    left: 0;
    width: 702px;
    text-align: center;
  }
  .contact-name {
    font-size: 48px;
    letter-spacing: 7px;
    font-weight: 400;
    margin: 0;
    line-height: 60px;
  }
  .contact-phone {
    font-size: 32px;
    letter-spacing: 5px;
    font-weight: 700;
    margin: 2px 0 0;
    line-height: 40px;
  }
  .contact-email {
    font-size: 37px;
    margin: 0;
    line-height: 46px;
  }
  .services {
    position: absolute;
    top: 730px;
    left: 120px;
  }
  .services-title {
    font-size: 48px;
    margin: 0 0 6px;
    font-weight: 400;
    line-height: 60px;
    text-decoration: underline;
    text-decoration-thickness: 2px;
    text-underline-offset: 7px;
  }
  .services-list {
    list-style: none;
    margin: 0;
    padding: 0;
  }
  .services-list li {
    position: relative;
    font-size: 39px;
    line-height: 42px;
    padding-left: 46px;
  }
  .services-list li::before {
    content: "";
    position: absolute;
    left: 2px;
    top: 12px;
    width: 12px;
    height: 12px;
    border-radius: 50%;
    background: var(--red);
    border: 4px solid #ffd5d7;
    box-shadow: 0 0 0 2px var(--red);
  }
  .footer-band {
    position: absolute;
    left: 0;
    bottom: 0;
    width: 702px;
    height: 100px;
    background: linear-gradient(90deg, var(--red) 0%, var(--red-soft) 50%, var(--grey-soft) 100%);
  }
</style>
</head>
<body>
  <main class="card">
    <header class="brand">
      <span class="brand-dot"></span>
      <span class="brand-name">Tidy Turf Crew</span>
    </header>

    <section class="contact">
      <h1 class="contact-name">Calvin Prewitt</h1>
      <p class="contact-phone">555-247-9061</p>
      <p class="contact-email">tidyturfcrew@mailvista.net</p>
    </section>

    <section class="services">
      <h2 class="services-title">Services offered</h2>
      <ul class="services-list">
        <li>Mowing</li>
        <li>Fertilization</li>
        <li>Aeration</li>
        <li>Bed &amp; tree maintenance</li>
        <li>and more.</li>
      </ul>
    </section>

    <div class="footer-band" role="img" aria-label="Decorative red and grey stripe band along the bottom edge"></div>
  </main>
</body>
</html>
```